We are a all around maintence company for outdoor services. Commercial and residential: mowing, sprinkler repairs, power washing, parking lot striping, tree trimming, gutters cleaning, pond cleaning,feeding and fertilizing, flower bed clean up and fence repair.

Industry/Entity Type

It Company

Contact Information for Business Card

Harbrook Yard Services
R.L. Vandermolt
Cell 555-312-4870
P.O. Box 4518
Millbrook,Co 80257
Office 555-629-3051
Fax 555-629-3057

```html
<!DOCTYPE html>
<html lang="en">
<head>
<meta charset="utf-8">
<title>Harbrook Yard Services – Business Card</title>
<link href="https://fonts.googleapis.com/css2?family=Montserrat:wght@300;400;600;700&display=swap" rel="stylesheet">
<style>
  :root {
    --page-bg: #e8e9eb;
    --card-white: #f4f4f3;
    --slate: #9a9b9d;
    --slate-light: #c9cacb;
    --leaf: #8cc63f;
    --ink-grey: #8e8f91;
    --text-white: #ffffff;
  }
  * { margin: 0; padding: 0; box-sizing: border-box; }
  html, body {
    width: 1200px;
    height: 800px;
    overflow: hidden;
    background: var(--page-bg);
    font-family: "Montserrat", Arial, sans-serif;
  }
  .business-card {
    position: absolute;
    left: 75px;
    top: 100px;
    width: 1050px;
    height: 600px;
    background: var(--card-white);
    box-shadow: 0 6px 24px rgba(0,0,0,0.12);
    overflow: hidden;
  }
  .card-shapes {
    position: absolute;
    inset: 0;
  }
  .brand {
    position: absolute;
    left: 120px;
    top: 118px;
    display: flex;
    align-items: center;
    gap: 16px;
  }
  .brand-dot {
    width: 26px;
    height: 26px;
    border-radius: 50%;
    background: var(--leaf);
  }
  .brand-name {
    font-weight: 600;
    font-size: 36px;
    color: var(--ink-grey);
    letter-spacing: 0.5px;
  }
  .person-name {
    position: absolute;
    left: 140px;
    top: 420px;
    font-size: 32px;
    color: var(--text-white);
    letter-spacing: 1px;
  }
  .person-name .initials { font-weight: 300; }
  .person-name .surname { font-weight: 700; text-transform: uppercase; }
  .contact {
    position: absolute;
    left: 700px;
    color: var(--text-white);
    font-weight: 400;
    font-size: 20px;
    line-height: 28px;
    display: flex;
    align-items: center;
    gap: 18px;
  }
  .contact-phone { top: 205px; }
  .contact-address { top: 300px; }
  .contact svg { flex: none; }
</style>
</head>
<body>
  <div class="business-card">
    <svg class="card-shapes" viewBox="0 0 1050 600" width="1050" height="600" aria-hidden="true">
      <polygon class="slate-block" points="0,288 493,288 700,500 610,588 0,588" fill="var(--slate)"/>
      <polygon class="slate-triangle" points="632,588 738,452 845,588" fill="var(--slate-light)" stroke="var(--card-white)" stroke-width="12"/>
      <polygon class="leaf-block" points="525,180 1050,180 1050,392 680,520 452,252" fill="var(--leaf)" stroke="var(--card-white)" stroke-width="12"/>
    </svg>

    <div class="brand">
      <span class="brand-dot"></span>
      <span class="brand-name">Harbrook Yard Services</span>
    </div>

    <div class="person-name"><span class="initials">R.L.</span> <span class="surname">Vandermolt</span></div>

    <div class="contact contact-phone">
      <svg width="20" height="20" viewBox="0 0 24 24" aria-hidden="true">
        <path fill="var(--text-white)" d="M6.6 10.8a15 15 0 0 0 6.6 6.6l2.2-2.2a1 1 0 0 1 1-.25 11.4 11.4 0 0 0 3.6.57 1 1 0 0 1 1 1V20a1 1 0 0 1-1 1A17 17 0 0 1 3 4a1 1 0 0 1 1-1h3.5a1 1 0 0 1 1 1c0 1.25.2 2.45.57 3.6a1 1 0 0 1-.25 1z"/>
      </svg>
      <div class="contact-lines">
        Cell 555-312-4870<br>
        Office 555-629-3051<br>
        Fax 555-629-3057
      </div>
    </div>

    <div class="contact contact-address">
      <svg width="20" height="24" viewBox="0 0 20 26" aria-hidden="true">
        <path fill="var(--text-white)" d="M10 0a9 9 0 0 0-9 9c0 6.8 9 17 9 17s9-10.2 9-17a9 9 0 0 0-9-9zm0 12.5A3.5 3.5 0 1 1 10 5.5a3.5 3.5 0 0 1 0 7z"/>
      </svg>
      <div class="contact-lines">
        P.O. Box 4518<br>
        Millbrook,Co 80257
      </div>
    </div>
  </div>
</body>
</html>
```